Book Cover Design Project

I am writing a book called Sisters & Figs. It may be a combination of traditional publishing, an ebook, and/or self-publishing. This will be the first book in a series of 4 books. The audience are 50ish women (40 year olds will probably read it to) who are successful, accomplished and who have made lemonade out of lemons in life, and now I am encouraging them to take that lemon in hand and instead of making lemonade, squeeze the life out of that lemon and get the zest that life still has to offer them. "Rise Up Today" is a subtitle of the book. From the book cover design, I also hope to derive a logo for journals and a T-Shirt design that rocks. These women are sexy, sassy, smart, and sensational and are looking for the adventure that life has to offer them, not rocking chairs. So for a design I am looking for it to incorporate women, a woman's hand squeezing a lemon, maybe lots of lemons, lots of yellow, squeezing a lemon, squeezing life, fun, adventure and excitement in the book cover design. I want it to POP right off the book and WOW women so that the book will scream "buy me" just because of the cover and be surprised to the content it has to offer. I am looking for absolutely spectacular cover that is absolutely sensational. I am hoping to use the same person for the logo, so keep that in mind.

Target Market(s)

women 40 - 60

Industry/Entity Type

Publishing

Requirements
Must have
• Women, Lemons, Excitement, Sexy, Classy, Sensational, the color yellow
Nice to have
• maybe the hand of a woman squeezing a lemon and juice coming out

maybe a woman, several, or a group of women in a barrel, pool or mansion full of lemons

```html
<!DOCTYPE html>
<html lang="en">
<head>
<meta charset="utf-8">
<title>Sisters &amp; Figs – Book Cover Spread</title>
<link rel="stylesheet" href="https://fonts.googleapis.com/css2?family=Roboto:wght@100;300;400;500&family=Source+Sans+3:wght@400&display=swap">
<style>
  :root {
    --page-bg: #ececec;
    --yellow: #f7c51a;
    --yellow-light: #fbd84a;
    --yellow-pale: #fde78a;
    --lemon-deep: #e8b10c;
    --ink: #111111;
    --white: #ffffff;
    --photo-dark: #2a2416;
    --photo-warm: #c79612;
  }
  * { box-sizing: border-box; margin: 0; padding: 0; }
  html, body { width: 1200px; height: 848px; overflow: hidden; }
  body {
    background: var(--page-bg);
    position: relative;
    font-family: "Source Sans 3", Arial, sans-serif;
    color: var(--ink);
  }
  .spread { position: absolute; top: 80px; left: 96px; width: 1008px; height: 653px; }
  .panel { position: absolute; top: 0; height: 653px; background: var(--yellow-light); overflow: hidden; }
  .back-cover { left: 0; width: 463px; }
  .spine { left: 474px; width: 58px; }
  .front-cover { left: 545px; width: 463px; }

  .lemon-photo {
    position: absolute; left: 0; width: 100%;
    background: radial-gradient(circle at 30% 30%, var(--yellow-pale), var(--yellow) 45%, var(--lemon-deep));
  }
  .stripes { position: absolute; left: 0; width: 100%; top: 526px; height: 20px; }
  .stripes span { position: absolute; left: 0; width: 100%; height: 3px; background: var(--lemon-deep); }
  .stripes span:nth-child(1) { top: 0; }
  .stripes span:nth-child(2) { top: 8px; }
  .stripes span:nth-child(3) { top: 16px; background: var(--yellow-pale); }
  .black-bar { position: absolute; height: 12px; background: var(--ink); top: 600px; }

  /* Back cover */
  .back-cover .lemon-photo { top: 0; height: 526px; }
  .blurb-card {
    position: absolute; left: 56px; top: 53px; width: 350px; height: 430px;
    background: rgba(255, 236, 140, 0.82);
    box-shadow: 0 1px 3px rgba(0,0,0,0.2);
    padding: 0 22px;
    font-size: 9.4px; line-height: 14.3px;
  }
  .blurb-card .card-heading { text-align: center; font-size: 12.5px; position: absolute; left: 0; width: 100%; }
  .blurb-card .card-heading.top { top: 10px; }
  .blurb-card .card-heading.bottom { top: 392px; }
  .double-rule { position: absolute; left: 53px; width: 244px; height: 5px; border-top: 1px solid var(--ink); border-bottom: 1px solid var(--ink); }
  .double-rule.top { top: 55px; }
  .double-rule.bottom { top: 355px; }
  .blurb-body { position: absolute; top: 107px; left: 16px; right: 22px; }
  .blurb-body p + p { margin-top: 14px; }
  .back-note { position: absolute; left: 27px; top: 557px; right: 20px; font-size: 9.4px; line-height: 14.3px; }
  .back-note.lower { top: 628px; }
  .back-cover .black-bar { left: 0; width: 100%; top: 598px; }

  /* Spine */
  .spine .spine-photo { position: absolute; top: 0; left: 0; width: 100%; height: 200px; background: linear-gradient(90deg, var(--photo-warm), var(--yellow) 60%, var(--photo-warm)); }
  .spine .spine-band { position: absolute; top: 200px; left: 0; width: 100%; height: 267px; background: linear-gradient(180deg, var(--photo-warm), var(--ink) 30%); }
  .spine .lemon-photo { top: 467px; height: 59px; }
  .spine-title {
    position: absolute; left: 29px; top: 333px;
    transform: translate(-50%, -50%) rotate(-90deg);
    white-space: nowrap; color: var(--white);
    font-family: "Roboto", Arial, sans-serif; font-weight: 300; font-size: 25px; letter-spacing: -0.5px;
  }
  .spine .black-bar { left: 0; width: 100%; top: 598px; }

  /* Front cover */
  .front-photo {
    position: absolute; top: 0; left: 0; width: 100%; height: 467px;
    background: radial-gradient(ellipse at 45% 40%, #6b5a2a 0%, var(--photo-dark) 45%, var(--ink) 75%),
                var(--photo-dark);
  }
  .front-photo-edge { position: absolute; top: 0; left: 0; width: 70px; height: 388px; background: linear-gradient(90deg, var(--yellow), rgba(247,197,26,0)); }
  .front-photo-right { position: absolute; top: 0; right: 0; width: 110px; height: 388px; background: linear-gradient(270deg, var(--yellow), rgba(247,197,26,0)); }
  .title {
    position: absolute; left: 8px; top: 185px; color: var(--white);
    font-family: "Roboto", Arial, sans-serif; line-height: 1;
  }
  .title .title-line1 { display: block; font-weight: 100; font-size: 86px; letter-spacing: -3px; }
  .title .title-line2 { display: block; font-weight: 500; font-size: 112px; letter-spacing: -4px; margin-top: -10px; }
  .subtitle {
    position: absolute; left: 10px; top: 410px; color: var(--white);
    font-family: "Roboto", Arial, sans-serif; font-weight: 300; font-size: 47px; letter-spacing: -1px; line-height: 1;
  }
  .front-cover .lemon-photo { top: 467px; height: 59px; }
  .tagline {
    position: absolute; left: 8px; font-family: "Roboto", Arial, sans-serif; font-weight: 400; font-size: 18.5px; letter-spacing: 0.3px;
  }
  .tagline.first { top: 557px; }
  .tagline.second { top: 603px; top: 621px; }
  .front-cover .black-bar.long { left: 0; width: 267px; }
  .front-cover .black-bar.short { left: 440px; width: 23px; }
  .author { position: absolute; left: 270px; top: 594px; font-family: "Roboto", Arial, sans-serif; font-weight: 400; font-size: 18px; letter-spacing: 0.2px; }
</style>
</head>
<body>
  <main class="spread">
    <section class="panel back-cover">
      <div class="lemon-photo" role="img" aria-label="Photograph of a pile of bright yellow lemons"></div>
      <div class="blurb-card">
        <p class="card-heading top">Lorem ipsum dolor sit amet,</p>
        <div class="double-rule top"></div>
        <div class="blurb-body">
          <p>Lorem ipsum dolor sit amet, consectetur adipiscing elit. Cras mattis porta orci, vel cursus erat euismod non. Mauris luctus, nulla nec ornare auctor, sem nibh facilisis turpis, vitae euismod mi erat eget tellus. Praesent magna eros, interdum imperdiet viverra sed, blandit et lacus. Aliquam dui elit, pharetra id dapibus non, fermentum in quam.</p>
          <p>Vivamus eros justo, facilisis nec dignissim sit amet, fermentum et lectus. Suspendisse potenti. Vestibulum rhoncus porttitor est eu eleifend. In hac habitasse platea dictumst. Integer viverra elit sit amet libero aliquet tincidunt. Nulla ante neque, posuere vel euismod ac, iaculis id risus. Pellentesque habitant morbi tristique senectus et netus et malesuada fames ac turpis egestas. In vehicula nulla at neque facilisis sagittis.</p>
          <p>Maecenas vitae quam eget ante aliquam euismod non dictum nulla. Pellentesque sapien diam, mattis viverra iaculis in, mattis id nibh. Cras felis lectus, tempor sed facilisis vel, tempor a lacus. Etiam bibendum turpis quis lectus mattis sit amet rutrum risus commodo.</p>
        </div>
        <div class="double-rule bottom"></div>
        <p class="card-heading bottom">Lorem ipsum dolor sit amet,</p>
      </div>
      <div class="stripes"><span></span><span></span><span></span></div>
      <p class="back-note">Lorem ipsum dolor sit amet, consectetur adipiscing elit. Cras mattis porta orci, vel cursus erat euismod non. Mauris luctus, nulla nec ornare auctor, sem nibh facilisis turpis, vitae euismod mi erat eget tellus.</p>
      <div class="black-bar"></div>
      <p class="back-note lower">Praesent magna eros, interdum imperdiet viverra sed,</p>
    </section>

    <section class="panel spine">
      <div class="spine-photo" role="img" aria-label="Blurred warm yellow photograph continuing from the front cover"></div>
      <div class="spine-band"></div>
      <p class="spine-title">SISTERS &amp;FIGS</p>
      <div class="lemon-photo" role="img" aria-label="Photograph of lemons"></div>
      <div class="stripes"><span></span><span></span><span></span></div>
      <div class="black-bar"></div>
    </section>

    <section class="panel front-cover">
      <div class="front-photo" role="img" aria-label="Photograph of a woman in a dark dress holding out a halved lemon, juice splashing"></div>
      <div class="front-photo-edge"></div>
      <div class="front-photo-right"></div>
      <h1 class="title"><span class="title-line1">SISTERS &amp;</span><span class="title-line2">FIGS</span></h1>
      <p class="subtitle">RISE UP TODAY</p>
      <div class="lemon-photo" role="img" aria-label="Photograph of whole and sliced lemons"></div>
      <div class="stripes"><span></span><span></span><span></span></div>
      <p class="tagline first">Begin YOUR Adventure</p>
      <div class="black-bar long"></div>
      <p class="author">By Marla J. Fenwick</p>
      <div class="black-bar short"></div>
      <p class="tagline second">Live YOUR Dream</p>
    </section>
  </main>
</body>
</html>
```